Produktbilder für LED-Birnen
Zielgruppe
Wir verkaufen LED Birnen.
Hallo Liebe Designer,
wir wollen unsere Produktbilder etwas umgestallten. Bitte schaut euch dazu die angehängten Bilder an. Generell sollen die neuen Grafiken auf den Produktbildern absolut exklusiv wirken und auf schwarzem und weißen Hintergrund funktionieren. Gerne dürft ihr zuerst einmal Bild1 designen um von uns eine Bewertung zu erhalten.
Wir brauchen die PSD mit allen Schriften usw., sodass wir später selbständig Abmessungen etc. ändern können.
Lampe7: Das sind unser Produktbilder, die als Vorlage dienen sollen. Der Störer '3x' soll später auch noch zu finden sein, darf aber auch verschoben werden.
Bild1: Das wird das Hauptbild werden. Neben den Symbolen auf dem Beispielbild soll hier auch 'German Company' mit einer kleinen Deutschlandflagge zu seihen sein
Bild2: Soll die Abmessungen der Lampe enthalten aber natürlich schicker gestaltet sein
Bild3: Soll den Inhalt enthalten, darf aber gerne mit anderen Symbolen umgesetzt werden.
Bild4: Muss auch die Daten enthalten soll aber wesentlich schöner gestaltet werden.
Viele Spaß beim designen!

```html
<!DOCTYPE html>
<html lang="de">
<head>
<meta charset="utf-8">
<title>LED-Birne – Produktbild</title>
<link href="https://fonts.googleapis.com/css2?family=Open+Sans:wght@400;600&display=swap" rel="stylesheet">
<style>
  :root {
    --paper: #ffffff;
    --ink: #000000;
    --amber-light: #f3e3c4;
    --amber-mid: #e2c48e;
    --brass: #b8902e;
    --flag-black: #000000;
    --flag-red: #dd0000;
    --flag-gold: #ffce00;
  }
  * { margin: 0; padding: 0; box-sizing: border-box; }
  html, body { width: 1200px; height: 655px; overflow: hidden; background: var(--paper); }
  body { font-family: "Open Sans", Arial, sans-serif; }
  .canvas { position: relative; width: 1200px; height: 655px; }
  .variant { position: absolute; top: 0; height: 655px; overflow: hidden; }
  .variant--light { left: 0; width: 599px; background: var(--paper); color: var(--ink); }
  .variant--dark { left: 599px; width: 601px; background: var(--ink); color: var(--ink); }

  .bulb {
    position: absolute; top: 43px; width: 262px; height: 586px;
    border-radius: 48% 48% 28% 28% / 30% 30% 14% 14%;
    background: linear-gradient(180deg, var(--amber-light) 0%, var(--amber-mid) 55%, #f2ead9 80%, var(--brass) 88%, #7a6020 100%);
  }
  .variant--light .bulb { left: 164px; }
  .variant--dark .bulb { left: 164px; box-shadow: 0 0 60px 40px rgba(255,255,255,0.95), 0 0 120px 70px rgba(255,255,255,0.55); }

  .feature-bar {
    position: absolute; top: 29px; left: 482px; width: 86px; height: 598px;
    display: flex; flex-direction: column; align-items: center;
  }
  .variant--light .feature-bar { background: var(--ink); color: var(--paper); }
  .variant--dark .feature-bar { background: var(--paper); color: var(--ink); }

  .feature { position: absolute; left: 0; width: 86px; display: flex; flex-direction: column; align-items: center; }
  .feature__label { font-size: 11px; letter-spacing: 1px; line-height: 12px; text-align: center; }
  .feature--dimmable { top: 50px; }
  .feature--dimmable svg { margin-bottom: 6px; }
  .feature--ce { top: 205px; }
  .feature--rohs { top: 370px; }
  .feature--origin { top: 480px; }
  .flag { width: 50px; height: 31px; display: flex; flex-direction: column; margin-bottom: 8px; }
  .variant--light .flag { outline: 1px solid var(--paper); }
  .flag span { flex: 1; }
  .flag .black { background: var(--flag-black); }
  .flag .red { background: var(--flag-red); }
  .flag .gold { background: var(--flag-gold); }
  .cert-mark { background: currentColor; }
  .cert-mark--round { width: 40px; height: 28px; border-radius: 14px; }
  .cert-mark--box { width: 64px; height: 40px; border-radius: 4px; }
</style>
</head>
<body>
<main class="canvas">
  <section class="variant variant--light">
    <div class="bulb" role="img" aria-label="Foto einer bernsteinfarbenen LED-Filament-Birne mit Spiralfaden und E27-Sockel"></div>
    <aside class="feature-bar">
      <div class="feature feature--dimmable">
        <svg width="50" height="22" viewBox="0 0 50 22"><path d="M3 21 A22 22 0 0 1 47 21 L41 21 A16 16 0 0 0 9 21 Z" fill="currentColor"/></svg>
        <span class="feature__label">DIMMABLE</span>
      </div>
      <div class="feature feature--ce"><div class="cert-mark cert-mark--round"></div></div>
      <div class="feature feature--rohs"><div class="cert-mark cert-mark--box"></div></div>
      <div class="feature feature--origin">
        <div class="flag"><span class="black"></span><span class="red"></span><span class="gold"></span></div>
        <span class="feature__label">German<br>Company</span>
      </div>
    </aside>
  </section>

  <section class="variant variant--dark">
    <div class="bulb" role="img" aria-label="Foto einer bernsteinfarbenen LED-Filament-Birne mit Spiralfaden und E27-Sockel, weiß hinterleuchtet"></div>
    <aside class="feature-bar">
      <div class="feature feature--dimmable">
        <svg width="50" height="22" viewBox="0 0 50 22"><path d="M3 21 A22 22 0 0 1 47 21 L41 21 A16 16 0 0 0 9 21 Z" fill="currentColor"/></svg>
        <span class="feature__label">DIMMABLE</span>
      </div>
      <div class="feature feature--ce"><div class="cert-mark cert-mark--round"></div></div>
      <div class="feature feature--rohs"><div class="cert-mark cert-mark--box"></div></div>
      <div class="feature feature--origin">
        <div class="flag"><span class="black"></span><span class="red"></span><span class="gold"></span></div>
        <span class="feature__label">German<br>Company</span>
      </div>
    </aside>
  </section>
</main>
</body>
</html>
```